mailer to distressed properties

Our business is a company that buys houses for cash that are in need of repairs. Need to create a post card to mail to homeowners to get them to call us to give them a price on their home for cash and purchase it. Would like a run down house on background and our company info so they could call us. Have a logo would like to incorporate in it. Want to get to the point across we can buy there home for cash on any condition and close quickly. We can also buy them if they have permit or violation issues. We also buy homes going into foreclosure so we can stop foreclosure. Company name is R & T Dwellings. P o box 829 Westmere my 11947. 631-482-9163. Email us at info@randtdwellings.example and our website Randtdwellings.example. Open to a lot of direct designs excited to see what you come up with. Anything else you can think we are open to see it. Email us with any other questions . Also can add fast closing and save no real estate commissions collected. We want it in color your choice. Also on font open to anything and size of font.

Target Market(s)

Run down and distressed properties

Industry/Entity Type

Construction Company

Font styles to use
Serif
Sans Serif

Requirements
Must have
• A background of a distressed home and our info how to call us
Nice to have
• Colorful and attractive
Should not have
• Nothing I can think of

```html
<!DOCTYPE html>
<html lang="en">
<head>
<meta charset="utf-8">
<title>R &amp; T Dwellings – Postcard</title>
<link href="https://fonts.googleapis.com/css2?family=Oswald:wght@500;600&family=Lato:wght@400;700&family=Montserrat:wght@600;700&display=swap" rel="stylesheet">
<style>
:root{
  --bg:#6b4a2c;
  --paper:#ffffff;
  --red:#e0222a;
  --green:#7dc242;
  --blue:#2f5fae;
  --bar-blue:#2a73b8;
  --ink:#1b1b1b;
  --dark:#262626;
  --muted:#333;
  --stamp:#333;
}
*{margin:0;padding:0;box-sizing:border-box}
html,body{width:907px;height:1200px;overflow:hidden;background:var(--bg)}
.card{position:absolute;left:63px;width:775px;height:500px;background:var(--paper);overflow:hidden;box-shadow:0 4px 14px rgba(0,0,0,.45)}
.card--front{top:70px}
.card--back{top:635px}
.card svg.shapes{position:absolute;inset:0;width:775px;height:500px}
.brand{position:absolute;font-family:'Montserrat',sans-serif;font-weight:700;color:var(--ink);white-space:nowrap}
.front-brand{left:12px;top:86px;font-size:17px}
.headline{position:absolute;left:14px;top:178px;font-family:'Oswald',sans-serif;font-weight:600;line-height:1;text-transform:uppercase}
.headline span{display:block}
.headline .l1{color:var(--blue);font-size:31px}
.headline .l2{color:var(--green);font-size:47px;margin-top:2px}
.headline .l3{color:var(--ink);font-size:38px;font-weight:500;margin-top:4px}
.call-bar{position:absolute;left:20px;top:330px;font-family:'Montserrat',sans-serif;font-weight:700;color:#fff;font-size:20px;letter-spacing:.5px}
.call-bar .num{font-family:'Oswald',sans-serif;font-weight:500;font-size:21px;margin-left:12px}
.cta{position:absolute;left:28px;top:392px;font-family:'Oswald',sans-serif;font-weight:600;text-transform:uppercase;white-space:nowrap}
.cta .small{color:var(--green);font-size:30px}
.cta .big{color:var(--red);font-size:40px;margin-left:6px}
.web{position:absolute;left:18px;top:473px;font-family:'Lato',sans-serif;color:#fff;font-size:13px;letter-spacing:4.5px}
.back-brand{left:342px;top:62px;font-size:19px}
.stamp{position:absolute;left:680px;top:13px;width:82px;height:97px;background:var(--stamp)}
.about{position:absolute;left:12px;top:172px;font-family:'Lato',sans-serif;color:var(--muted)}
.about h2{font-family:'Montserrat',sans-serif;font-weight:700;color:var(--red);font-size:20px;line-height:1.1;margin-bottom:2px}
.about p{font-size:10.8px;line-height:14px}
.about p span{display:block;white-space:nowrap}
.contacts{position:absolute;left:14px;top:332px;list-style:none;font-family:'Lato',sans-serif;font-size:11px;color:var(--muted);line-height:14px}
.contacts li{display:flex;align-items:center;gap:6px}
.contacts svg{width:9px;height:9px;flex:none}
</style>
</head>
<body>

<section class="card card--front">
  <svg class="shapes" viewBox="0 0 775 500">
    <defs>
      <linearGradient id="sceneTone" x1="0" y1="0" x2="0" y2="1">
        <stop offset="0" stop-color="#c7d6ea"/>
        <stop offset=".45" stop-color="#9aa3ad"/>
        <stop offset=".7" stop-color="#6f9a45"/>
        <stop offset="1" stop-color="#4f7d2e"/>
      </linearGradient>
    </defs>
    <polygon points="130,0 775,0 775,320 540,455" fill="url(#sceneTone)" role="img" aria-label="Photo of a large two-storey family house at dusk with a green lawn and a smiling agent presenting it"/>
    <polygon points="0,0 130,0 190,115 0,115" fill="var(--red)"/>
    <rect x="0" y="121" width="200" height="5" fill="var(--blue)"/>
    <rect x="0" y="130" width="205" height="5" fill="var(--green)"/>
    <polyline points="110,0 545,458 775,322" fill="none" stroke="var(--red)" stroke-width="9"/>
    <polyline points="94,0 541,472 775,335" fill="none" stroke="var(--green)" stroke-width="6"/>
    <polyline points="80,0 537,484 775,347" fill="none" stroke="var(--blue)" stroke-width="6"/>
    <polygon points="0,325 390,325 410,362 0,362" fill="var(--bar-blue)"/>
    <rect x="0" y="457" width="500" height="3" fill="var(--green)"/>
    <polygon points="0,465 495,465 512,500 0,500" fill="var(--dark)"/>
  </svg>
  <div class="brand front-brand">R &amp; T Dwellings</div>
  <h1 class="headline"><span class="l1">Quickly sell</span><span class="l2">Your house</span><span class="l3">Fast for cash</span></h1>
  <div class="call-bar">CALL US AT<span class="num">631-482-9163</span></div>
  <div class="cta"><span class="small">To get</span><span class="big">Started!</span></div>
  <div class="web">www.randtdwellings.example</div>
</section>

<section class="card card--back">
  <svg class="shapes" viewBox="0 0 775 500">
    <defs>
      <linearGradient id="planTone" x1="0" y1="0" x2="1" y2="1">
        <stop offset="0" stop-color="#d9d6d2"/>
        <stop offset=".6" stop-color="#eeeeee"/>
        <stop offset="1" stop-color="#ffffff"/>
      </linearGradient>
      <linearGradient id="roomTone" x1="0" y1="0" x2="0" y2="1">
        <stop offset="0" stop-color="#ffffff"/>
        <stop offset="1" stop-color="#ecebe8"/>
      </linearGradient>
    </defs>
    <rect x="0" y="0" width="340" height="170" fill="url(#planTone)" role="img" aria-label="Illustration of a house under construction cut away over architectural floor plans"/>
    <rect x="0" y="300" width="300" height="130" fill="url(#roomTone)" role="img" aria-label="Faded photo of a bright furnished living room"/>
    <polyline points="610,0 245,478 0,392" fill="none" stroke="var(--red)" stroke-width="9"/>
    <polyline points="628,0 248,489 0,412" fill="none" stroke="var(--green)" stroke-width="6"/>
    <polyline points="642,0 252,500 0,430" fill="none" stroke="var(--blue)" stroke-width="6"/>
  </svg>
  <div class="brand back-brand">R &amp; T Dwellings</div>
  <div class="stamp" aria-label="Stamp area"></div>
  <div class="about">
    <h2>About Us</h2>
    <p>
      <span>R &amp; T Dwellings understands the challenges homeowners face when trying to sell</span>
      <span>their house. If you want to avoid the lengthy process and high commissions</span>
      <span>of using a real estate agent, or are in a tough situation and need to sell</span>
      <span>your house fast, R &amp; T Dwellings will remove the biggest obstacles</span>
      <span>&nbsp;you'll face.</span>
      <span>We'll give you top dollar for your house, accept it in any condition,</span>
      <span>and take you through the whole process quickly. Our team is</span>
      <span>local and made up of licensed and insured home builders and</span>
      <span>real estate professionals who have a proven track record.</span>
    </p>
  </div>
  <ul class="contacts">
    <li><svg viewBox="0 0 10 10"><path d="M5 0a3.5 3.5 0 0 0-3.5 3.5C1.5 6 5 10 5 10s3.5-4 3.5-6.5A3.5 3.5 0 0 0 5 0zm0 5a1.4 1.4 0 1 1 0-2.8A1.4 1.4 0 0 1 5 5z" fill="var(--green)"/></svg>P o box 829 Westmere my 11947</li>
    <li><svg viewBox="0 0 10 10"><rect width="10" height="10" rx="2" fill="var(--green)"/><path d="M3 2.5l1 1.5-.6.7a4 4 0 0 0 2 2l.7-.6 1.5 1-.6 1c-2.5-.2-4.8-2.5-5-5z" fill="#fff"/></svg>631-482-9163</li>
    <li><svg viewBox="0 0 10 10"><rect x=".5" y="2" width="9" height="6" fill="none" stroke="var(--green)"/><path d="M.5 2L5 5.5 9.5 2" fill="none" stroke="var(--green)"/></svg>info@randtdwellings.example</li>
    <li><svg viewBox="0 0 10 10"><circle cx="5" cy="5" r="4.5" fill="none" stroke="var(--green)"/><path d="M.5 5h9M5 .5c-2.5 3-2.5 6 0 9M5 .5c2.5 3 2.5 6 0 9" fill="none" stroke="var(--green)" stroke-width=".7"/></svg>Randtdwellings.example</li>
  </ul>
</section>

</body>
</html>
```